Brochure Design Project

We are a payroll company. We offer a wide variety of products and services:
1. Payroll Processing
2. Employee Direct Deposit
3. Time and attendance
4. HR services
5. Employee Employee Benefits

I'd like to develop a one page template that uses a combination of our logo (attached), colors (attached) and possible a picture. The picture could be shown as an option as it may change based on the product or service.

Target Market(s)

Adults in the United States ages 22-50. Typically these people are accountants, human resource professionals or entrepreneurs. The payroll industry is dominated by 3 large payroll processors, QLM, Wendrafy and Tolvarex. These companies are very impersonal and make it difficult to resolve issues when they arise. We have grown to over 400 clients by being the opposite of the big guys,

Industry/Entity Type

It Company

Font styles to use
Sans Serif

Requirements
Must have
• The brochure can be one or two pages.
Nice to have
• I'll know it when I see it but I can't describe it. I have attached a few brochures that have caught my eye.
Should not have
• No cartoons. No money signs. Hip, new, fresh are words I'd use to describe the winning product. Of the three people I described in my target market, the entrepreneur is the market I'd most like to target.

```html
<!DOCTYPE html>
<html lang="en">
<head>
<meta charset="utf-8">
<title>Ledgerly Crew – One Page Brochure</title>
<link href="https://fonts.googleapis.com/css2?family=Open+Sans:ital,wght@0,400;0,600;0,700;1,700&display=swap" rel="stylesheet">
<style>
  :root {
    --navy: #22336a;
    --green: #8cc043;
    --grey: #6f7173;
    --white: #ffffff;
    --backdrop: #e9e9e9;
    --photo-dark: #3f5670;
    --photo-light: #b9c6d3;
  }
  html, body {
    margin: 0;
    width: 1200px;
    height: 1000px;
    overflow: hidden;
    background: var(--backdrop);
    font-family: "Open Sans", Arial, sans-serif;
  }
  .brochure {
    position: absolute;
    left: 80px;
    top: 160px;
    width: 1040px;
    height: 680px;
    background: var(--white);
    box-shadow: 0 6px 24px rgba(0,0,0,0.18);
    overflow: hidden;
  }
  .brochure__shapes {
    position: absolute;
    inset: 0;
  }
  .brand-name {
    position: absolute;
    margin: 0;
    color: var(--navy);
    font-weight: 700;
    letter-spacing: -0.5px;
    line-height: 1;
  }
  .brand-name--header { left: 40px; top: 40px; font-size: 40px; }
  .brand-name--footer { right: 30px; bottom: 30px; font-size: 26px; }
  .intro {
    position: absolute;
    left: 60px;
    top: 158px;
    width: 500px;
    color: var(--white);
    font-size: 11.5px;
    line-height: 1.45;
  }
  .intro p { margin: 0 0 12px; }
  .tagline {
    position: absolute;
    left: 40px;
    top: 412px;
    margin: 0;
    color: var(--white);
    font-size: 36px;
    font-weight: 700;
    font-style: italic;
    line-height: 1.4;
  }
  .web-address {
    position: absolute;
    left: 150px;
    top: 500px;
    margin: 0;
    color: var(--navy);
    font-size: 13px;
    font-weight: 600;
    letter-spacing: 3px;
  }
  .photo-slot {
    position: absolute;
    left: 650px;
    top: 225px;
    width: 390px;
    height: 245px;
    background: linear-gradient(135deg, var(--photo-dark), var(--photo-light) 60%, var(--photo-dark));
  }
  .service-note {
    position: absolute;
    left: 680px;
    top: 480px;
    width: 340px;
    margin: 0;
    color: var(--white);
    font-size: 12.5px;
    line-height: 1.4;
    text-align: justify;
  }
</style>
</head>
<body>
  <main class="brochure">
    <svg class="brochure__shapes" width="1040" height="680" viewBox="0 0 1040 680" aria-hidden="true">
      <polygon class="accent-wedge" points="430,120 640,120 640,50" fill="var(--green)"/>
      <rect class="intro-panel" x="0" y="120" width="640" height="350" fill="var(--navy)"/>
      <polygon class="footer-band" points="400,470 1040,470 1040,605 640,565" fill="var(--green)"/>
      <polygon class="tagline-band" points="0,405 300,405 365,470 0,470" fill="var(--grey)"/>
    </svg>

    <h1 class="brand-name brand-name--header">Ledgerly Crew</h1>

    <section class="intro">
      <p>Our Managed Services package is Norvane's 'outsourcing service' and is an excellent way to assist our clients with delivering against all their internal business's I.T needs. What makes this particular service unique is it greatly reduces the need for expensive internal I.T resources.</p>
      <p>Our Managed Services package is Norvane's 'outsourcing service' and is an excellent way to assist our clients with delivering against all their internal business's I.T needs. What makes this particular service unique is it greatly reduces (and often removes) the need for expensive internal I.T resources.</p>
      <p>To assist our clients with delivering against all their internal business's I.T needs. What makes this service unique is it greatly reduces the need for expensive internal I.T resources.</p>
    </section>

    <p class="tagline">a Payroll Partner.</p>
    <p class="web-address">www.ledgerlycrew.com</p>

    <div class="photo-slot" role="img" aria-label="Photo of a hand pressing keys on a calculator, in blue-grey tones"></div>

    <p class="service-note">Our Managed Services package is Norvane's 'outsourcing service' and is an excellent way to assist our clients with delivering against all their internal business's I.T needs.</p>

    <p class="brand-name brand-name--footer">Ledgerly Crew</p>
  </main>
</body>
</html>
```